Postcard Design Project

We sells Laser Printer Ink and Toners, We also sells on Brindlo Market Place, Need a post card for these brindlo contact to start buying through our website instead of Brindlo. Company Name: Ky Office Wares LLC, website is www.kyprintvo.com phone#718-555-0142

```html
<!DOCTYPE html>
<html lang="en">
<head>
<meta charset="utf-8">
<title>Ky Office Wares – Postcard</title>
<link rel="stylesheet" href="https://fonts.googleapis.com/css2?family=Alfa+Slab+One&family=Saira+Condensed:wght@500;600;700&family=Nunito:wght@300;700;800&display=swap">
<style>
  :root {
    --page: #e9ebe8;
    --white: #ffffff;
    --ink: #141414;
    --sky: #29a9e0;
    --blue: #1e8fd6;
    --deep-blue: #1b5fb3;
    --purple: #6b3da3;
    --magenta: #e2348f;
    --orange: #f7941d;
    --red: #e5412d;
    --yellow: #ffe600;
  }
  * { margin: 0; padding: 0; box-sizing: border-box; }
  html, body { width: 1200px; height: 900px; overflow: hidden; background: var(--page); }
  body { position: relative; font-family: "Nunito", sans-serif; }

  .card {
    position: absolute; width: 600px; height: 400px;
    background: var(--white); overflow: hidden;
    box-shadow: 0 4px 14px rgba(0,0,0,.18);
  }
  .card--back { left: 40px; top: 40px; }
  .card--front { left: 560px; top: 460px; }

  .brand {
    position: absolute; display: flex; align-items: center; gap: 5px;
    font-family: "Saira Condensed", sans-serif; font-weight: 700; color: var(--ink);
    white-space: nowrap;
  }
  .brand__dot { border-radius: 50%; background: var(--magenta); flex: none; }

  /* ---------- back side ---------- */
  .back-panel { position: absolute; left: 0; top: 0; width: 296px; height: 400px; }
  .back-panel .brand { left: 8px; top: 20px; font-size: 14px; line-height: 16px; }
  .back-panel .brand__dot { width: 11px; height: 11px; }
  .back-headline {
    position: absolute; left: 116px; top: 23px; white-space: nowrap;
    font-family: "Alfa Slab One", serif; font-size: 12.5px; line-height: 16px; color: var(--ink);
  }
  .back-art { position: absolute; left: 0; top: 62px; width: 296px; height: 338px; }
  .back-copy { position: absolute; left: 12px; top: 278px; width: 280px; }
  .back-copy__title {
    font-family: "Alfa Slab One", serif; font-size: 10.3px; color: var(--yellow); white-space: nowrap;
  }
  .back-copy__body {
    margin-top: 6px; font-weight: 300; font-size: 14px; line-height: 16px; color: var(--yellow);
  }
  .back-copy__label { margin-top: 13px; font-size: 9px; color: var(--white); font-weight: 300; line-height: 10px; }
  .back-copy__value { font-size: 11px; font-weight: 800; color: var(--white); line-height: 13px; }
  .back-copy__label--small { margin-top: 1px; font-size: 8.5px; }

  /* ---------- front side ---------- */
  .card--front .brand { left: 12px; top: 36px; font-size: 22px; line-height: 26px; }
  .card--front .brand__dot { width: 18px; height: 18px; }
  .front-headline {
    position: absolute; left: 205px; top: 26px;
    font-family: "Alfa Slab One", serif; font-size: 27px; line-height: 36px; color: var(--ink);
    white-space: nowrap;
  }
  .front-subline {
    position: absolute; left: 205px; top: 66px;
    font-family: "Nunito", sans-serif; font-weight: 300; font-size: 18px; color: var(--sky);
    white-space: nowrap; letter-spacing: -.2px;
  }
  .front-art { position: absolute; left: 0; top: 0; width: 600px; height: 400px; }
  .front-offer {
    position: absolute; left: 27px; top: 160px;
    font-family: "Saira Condensed", sans-serif; font-weight: 600; font-size: 25px; line-height: 27px;
    color: var(--white);
  }
  .front-visit { position: absolute; left: 27px; top: 292px; font-family: "Saira Condensed", sans-serif; }
  .front-visit__label { font-weight: 600; font-size: 18px; color: var(--yellow); line-height: 20px; }
  .front-visit__url { font-family: "Nunito", sans-serif; font-weight: 800; font-size: 25px; color: var(--yellow); line-height: 30px; white-space: nowrap; }
  .front-call {
    position: absolute; left: 440px; top: 318px; transform: rotate(7deg); transform-origin: left top;
    font-family: "Alfa Slab One", serif; color: var(--yellow); white-space: nowrap;
  }
  .front-call__label { font-size: 16px; line-height: 20px; }
  .front-call__phone { font-size: 19px; line-height: 24px; }
</style>
</head>
<body>

  <!-- Address side -->
  <section class="card card--back" aria-label="Postcard address side">
    <div class="back-panel">
      <div class="brand"><span class="brand__dot"></span>Ky Office Wares</div>
      <div class="back-headline">GOT DIRTY PRINTER?</div>

      <svg class="back-art" viewBox="0 0 296 338" aria-hidden="true">
        <defs>
          <linearGradient id="backPanel" x1="0" y1="0" x2="1" y2="1">
            <stop offset="0" stop-color="#6b3da3"/>
            <stop offset=".55" stop-color="#1ea5e0"/>
            <stop offset="1" stop-color="#1b6fc0"/>
          </linearGradient>
          <linearGradient id="backPhoto" x1="0" y1="0" x2="1" y2="1">
            <stop offset="0" stop-color="#d5d8dc"/>
            <stop offset="1" stop-color="#8e939a"/>
          </linearGradient>
          <linearGradient id="backArc" x1="0" y1="0" x2="1" y2="0">
            <stop offset="0" stop-color="#e5412d"/>
            <stop offset=".5" stop-color="#f7941d"/>
            <stop offset="1" stop-color="#e5412d"/>
          </linearGradient>
        </defs>
        <rect x="0" y="0" width="296" height="338" fill="url(#backPanel)"/>
        <rect x="0" y="0" width="296" height="186" fill="url(#backPhoto)" role="img" aria-label="Photo of a home inkjet printer on a desk by a window"/>
        <path d="M0 0 H296 V14 Q150 -4 0 12 Z" fill="#1e8fd6"/>
        <path d="M0 12 Q150 -4 296 14 V30 Q150 14 0 30 Z" fill="url(#backArc)"/>
        <path d="M0 166 Q150 150 296 176 V190 H0 Z" fill="#e2348f"/>
      </svg>

      <div class="back-copy">
        <div class="back-copy__title">GET A TECHNICIAN IN YOUR OFFICE TODAY</div>
        <p class="back-copy__body">Also Check Out Our Unbeatable<br>Ink and Toner Online Pricrs.</p>
        <div class="back-copy__label">CALL TODAY</div>
        <div class="back-copy__value">718-555-0142</div>
        <div class="back-copy__label back-copy__label--small">Visit us online</div>
        <div class="back-copy__value">www.kyprintvo.com</div>
      </div>
    </div>
  </section>

  <!-- Picture side -->
  <section class="card card--front" aria-label="Postcard front side">
    <svg class="front-art" viewBox="0 0 600 400" aria-hidden="true">
      <defs>
        <linearGradient id="frontPanel" x1="0" y1="0" x2="1" y2="1">
          <stop offset="0" stop-color="#6b3da3"/>
          <stop offset=".45" stop-color="#1ea5e0"/>
          <stop offset="1" stop-color="#1b5fb3"/>
        </linearGradient>
        <linearGradient id="frontArc" x1="0" y1="0" x2="1" y2="0">
          <stop offset="0" stop-color="#f7941d"/>
          <stop offset=".4" stop-color="#f7b267"/>
          <stop offset=".75" stop-color="#f7941d"/>
          <stop offset="1" stop-color="#e5412d"/>
        </linearGradient>
        <linearGradient id="frontPink" x1="0" y1="0" x2="1" y2="1">
          <stop offset="0" stop-color="#f27bb5"/>
          <stop offset="1" stop-color="#c2187a"/>
        </linearGradient>
        <linearGradient id="frontPhoto" x1="0" y1="0" x2="1" y2="1">
          <stop offset="0" stop-color="#d9dadb"/>
          <stop offset=".6" stop-color="#6f7378"/>
          <stop offset="1" stop-color="#3b3e42"/>
        </linearGradient>
        <linearGradient id="frontTag" x1="0" y1="0" x2="1" y2="1">
          <stop offset="0" stop-color="#29a9e0"/>
          <stop offset="1" stop-color="#1e7fd0"/>
        </linearGradient>
      </defs>

      <rect x="280" y="146" width="320" height="182" fill="url(#frontPhoto)" role="img" aria-label="Photo of an open wide-format printer with its ink cartridges exposed"/>

      <path d="M170 128 Q400 88 600 140 V156 Q400 106 190 142 Z" fill="#1e8fd6"/>
      <path d="M185 134 Q400 100 600 148 V168 Q400 118 200 150 Z" fill="url(#frontArc)"/>

      <path d="M216 148 L350 148 L284 300 Z" fill="url(#frontPink)"/>

      <path d="M0 107 L164 87 L196 122 L330 370 Q160 376 0 400 Z" fill="url(#frontPanel)"/>
      <path d="M170 100 L330 370 L300 372 L150 104 Z" fill="#1ea5e0" opacity=".55"/>

      <path d="M305 318 L410 310 L420 340 L330 350 Z" fill="#f7941d"/>
      <path d="M403 307 L600 326 V397 L442 378 Z" fill="url(#frontTag)"/>
    </svg>

    <div class="brand"><span class="brand__dot"></span>Ky Office Wares</div>
    <div class="front-headline">GOT DIRTY PRINTER?</div>
    <div class="front-subline">GET A TECHNICIAN IN YOUR OFFICE TODAY</div>

    <p class="front-offer">Also Check Out<br>Our Unbeatable<br>Ink and Toner<br>Online Pricrs.</p>

    <div class="front-visit">
      <div class="front-visit__label">Visit us online</div>
      <div class="front-visit__url">www.kyprintvo.com</div>
    </div>

    <div class="front-call">
      <div class="front-call__label">CALL TODAY</div>
      <div class="front-call__phone">718-555-0142</div>
    </div>
  </section>

</body>
</html>
```